Startup in search for creative and funky label for a food product

We, Vindrossa Food Lab need a label for a new product: extra virgin oil from roasted sunflower seeds. The oil is produced at family gardens in sunny Kakheti region in Western Georgia.
Our goal is to introduce this new exclusive product, unknown in Western Europe. The test panels in Sweden liked the product and we hope to sell both for foodies and general public.
The feeling of the label shoud be both creative and exclusive. Maybe even funky, please see the file attached.

We would like to have the label in English and Swedish. Maybe we can do it in English first, since not all of you would understand Swedish, the Swedish design would be identical. The document below has both English and Swedish text.

We attachthe image of the bottle, please do not consider the label on the bottle, it is just an example.

Target Market(s)

General Market in Sweden and Europe. First priority: foddies, restaurants, specialized food stores.

Industry/Entity Type

Online Shopping

Requirements
Must have
• We would need the design in two languages, the same design for Swedish and English, but two separated labels. Once we agree on the English version, we can do the same for Swedish.
Nice to have
• Feeling of locally grown sunflowers, eye-catching.
Should not have
• Classic design for oil

```html
<!DOCTYPE html>
<html lang="en">
<head>
<meta charset="utf-8">
<title>Vindrossa Food Lab – Extra Virgin Oil from Roasted Sunflower Seed</title>
<link rel="stylesheet" href="https://fonts.googleapis.com/css2?family=Play:wght@400;700&family=Open+Sans:ital,wght@0,400;0,600;1,400&display=swap">
<style>
  :root {
    --teal: #4fb0b8;
    --teal-deep: #4a9fae;
    --sun-yellow: #ecc730;
    --petal-gold: #d9a43a;
    --petal-light: #f3dc6a;
    --ink: #1d1c1e;
    --sky-blue: #4cc3ee;
    --leaf-green: #1f5a3c;
    --white: #ffffff;
  }
  * { box-sizing: border-box; margin: 0; padding: 0; }
  html, body {
    width: 830px;
    height: 1200px;
    overflow: hidden;
    background: var(--white);
  }
  .label {
    position: relative;
    width: 830px;
    height: 1200px;
    overflow: hidden;
    background: radial-gradient(ellipse at 85% 70%, var(--teal-deep) 0%, var(--teal) 55%);
    font-family: "Open Sans", sans-serif;
    color: var(--ink);
  }
  .sunflower-art {
    position: absolute;
    left: 0;
    top: 0;
    width: 830px;
    height: 600px;
  }
  .brand {
    position: absolute;
    left: 270px;
    top: 50px;
    width: 290px;
    height: 290px;
    border-radius: 50%;
    background: var(--ink);
    display: flex;
    align-items: center;
    justify-content: center;
    text-align: center;
  }
  .brand-name {
    font-family: "Play", sans-serif;
    font-weight: 400;
    font-size: 34px;
    line-height: 1.15;
    letter-spacing: 2px;
    color: var(--sun-yellow);
    width: 200px;
  }
  .title-band {
    position: absolute;
    left: 0;
    width: 830px;
    display: flex;
    align-items: center;
    justify-content: center;
    font-family: "Play", sans-serif;
  }
  .title-main {
    top: 605px;
    height: 96px;
    background: var(--sun-yellow);
    font-size: 56px;
    letter-spacing: 4px;
  }
  .title-from {
    top: 701px;
    height: 70px;
    background: var(--ink);
    color: var(--white);
    font-size: 46px;
    letter-spacing: 2px;
  }
  .title-from .roasted {
    color: var(--sky-blue);
    font-weight: 700;
    margin-left: 20px;
  }
  .title-seed {
    top: 771px;
    height: 71px;
    background: var(--sun-yellow);
    font-size: 40px;
    letter-spacing: 5px;
  }
  .details {
    position: absolute;
    left: 0;
    top: 870px;
    width: 830px;
    text-align: center;
  }
  .grade {
    font-size: 32px;
    font-weight: 600;
    letter-spacing: 5px;
    line-height: 44px;
  }
  .origin {
    font-size: 29px;
    font-style: italic;
    color: var(--leaf-green);
    line-height: 44px;
  }
  .qualities {
    margin-top: 40px;
    font-size: 33px;
    line-height: 44px;
  }
  .volume {
    margin-top: 30px;
    font-size: 25px;
  }
</style>
</head>
<body>
  <main class="label">
    <svg class="sunflower-art" viewBox="0 0 830 600" role="img" aria-label="Large illustrated sunflower in yellow and golden watercolour petals radiating from the centre">
      <defs>
        <radialGradient id="sunflower-glow" cx="415" cy="190" r="440" gradientUnits="userSpaceOnUse">
          <stop offset="0" stop-color="var(--petal-light)"/>
          <stop offset="0.55" stop-color="var(--sun-yellow)"/>
          <stop offset="0.85" stop-color="var(--petal-gold)"/>
          <stop offset="1" stop-color="var(--petal-gold)" stop-opacity="0"/>
        </radialGradient>
      </defs>
      <rect x="0" y="0" width="830" height="600" fill="url(#sunflower-glow)"/>
    </svg>

    <div class="brand">
      <span class="brand-name">Vindrossa Food Lab</span>
    </div>

    <h1 class="title-band title-main">Extra Virgin Oil</h1>
    <p class="title-band title-from">from<span class="roasted">ROASTED</span></p>
    <p class="title-band title-seed">sunflower seed</p>

    <section class="details">
      <p class="grade">Premium</p>
      <p class="origin">from family gardens in Georgia</p>
      <p class="qualities">Unrefined<br>All natural</p>
      <p class="volume">260 ml</p>
    </section>
  </main>
</body>
</html>
```